Medical Device Company- Ankle Brace package

We need help redesigning our ankle brace product bag. We've attached a previous version of it that includes our old company name (clear path medical) and the color teal as an accent, which we are not using anymore. We prefer the package color to be in the dark grey but we are open to other colors such as black, white, light grey and slate blue. We are looking for design elements, creativity and a better layout.
- New Company Name = Valdimex
- Package Size 11 inches x 8.5 inches.
- We do not need sizing on the bag but need a spot to place a sticker.
Industry/Entity Type
medical devices

```html
<!DOCTYPE html>
<html lang="en">
<head>
<meta charset="utf-8">
<title>Valdimex Ankle Brace Pouch</title>
<link href="https://fonts.googleapis.com/css2?family=Roboto+Condensed:wght@400;700&family=Oswald:wght@600&family=Barlow:wght@500&display=swap" rel="stylesheet">
<style>
  :root {
    --canvas: #ffffff;
    --slate-top: #536a78;
    --slate-bottom: #364b58;
    --photo-dark: #1f2124;
    --photo-mid: #2c2e31;
    --ink-white: #ffffff;
    --tag-light: #d9dcdf;
    --tag-dark: #9ca1a6;
    --block-black: #111315;
    --badge-white: #f4f5f6;
    --badge-ink: #1c1f22;
  }
  * { margin: 0; padding: 0; box-sizing: border-box; }
  html, body { width: 1126px; height: 1200px; overflow: hidden; background: var(--canvas); }
  .canvas { position: relative; width: 1126px; height: 1200px; }

  .pouch {
    position: absolute; left: 229px; top: 230px; width: 669px; height: 842px;
    border-radius: 18px;
    background: linear-gradient(180deg, var(--slate-top) 0%, #4a606d 45%, var(--slate-bottom) 100%);
    overflow: hidden;
  }
  .pouch__notch { position: absolute; top: 62px; width: 10px; height: 16px; background: var(--canvas); }
  .pouch__notch--left { left: -4px; border-radius: 0 8px 8px 0; }
  .pouch__notch--right { right: -4px; border-radius: 8px 0 0 8px; }

  .product-photo {
    position: absolute; left: 300px; top: 0; width: 369px; height: 690px;
    border-radius: 0 0 0 24px;
    background: linear-gradient(160deg, var(--photo-mid) 0%, var(--photo-dark) 60%, #3a3d41 100%);
    opacity: 0.9;
  }

  .brand { position: absolute; left: 56px; top: 150px; display: flex; align-items: center; gap: 14px; }
  .brand__mark { width: 36px; height: 36px; background: var(--ink-white); border-radius: 4px; }
  .brand__name {
    font-family: "Barlow", sans-serif; font-weight: 500; font-size: 33px;
    color: var(--ink-white); letter-spacing: 0.5px;
  }

  .title {
    position: absolute; left: 54px; top: 229px;
    font-family: "Oswald", sans-serif; font-weight: 600; font-size: 76px;
    line-height: 73px; color: var(--ink-white); letter-spacing: 1px;
  }
  .subtitle {
    position: absolute; left: 56px; top: 380px;
    font-family: "Roboto Condensed", sans-serif; font-weight: 700; font-size: 25px;
    color: var(--ink-white); letter-spacing: 0.3px;
  }

  .size-tag {
    position: absolute; right: 0; top: 307px; width: 161px; height: 37px;
    border-radius: 6px 0 0 6px;
    background: linear-gradient(90deg, var(--tag-light), var(--tag-dark));
    font-family: "Roboto Condensed", sans-serif; font-size: 25px;
    color: var(--badge-ink); line-height: 37px; padding-left: 22px; letter-spacing: 1px;
  }

  .contents {
    position: absolute; left: 56px; top: 732px; width: 117px; height: 110px;
    background: linear-gradient(180deg, #25282b, var(--block-black));
    padding: 9px 0 0 15px;
    font-family: "Roboto Condensed", sans-serif; font-size: 17px; line-height: 20px;
    color: var(--ink-white);
  }
  .contents strong { font-weight: 700; }

  .approval { position: absolute; left: 445px; top: 746px; width: 170px; height: 52px; }
  .approval__pill {
    position: absolute; left: 0; top: 10px; width: 140px; height: 38px;
    background: var(--badge-white); border-radius: 19px;
    font-family: "Roboto Condensed", sans-serif; font-size: 11px; line-height: 12px;
    color: var(--badge-ink); text-align: right; padding: 9px 26px 0 0;
  }
  .approval__label {
    position: absolute; left: 42px; top: 0; width: 92px; height: 14px;
    background: var(--badge-ink); border-radius: 7px 7px 0 0;
    font-family: "Roboto Condensed", sans-serif; font-size: 10px; line-height: 14px;
    color: var(--ink-white); text-align: center;
  }
  .approval__seal {
    position: absolute; left: 120px; top: 0; width: 50px; height: 50px; border-radius: 50%;
    background: radial-gradient(circle at 40% 35%, #ffffff, #c9cdd0);
    border: 3px solid #e8eaeb;
  }
</style>
</head>
<body>
<main class="canvas">
  <section class="pouch">
    <div class="product-photo" role="img" aria-label="Product photo: foot in a white sock wearing the black compression ankle brace with adjustable strap"></div>

    <span class="pouch__notch pouch__notch--left"></span>
    <span class="pouch__notch pouch__notch--right"></span>

    <div class="brand">
      <span class="brand__mark"></span>
      <span class="brand__name">Valdimex</span>
    </div>

    <h1 class="title">ANKLE<br>BRACE</h1>
    <p class="subtitle">WITH COMPRESSION</p>

    <div class="size-tag">Medium</div>

    <div class="contents"><strong>1 BRACE &amp;</strong><br>ADJUSTABLE<br>STRAP</div>

    <div class="approval">
      <div class="approval__pill">AN ORTHOPEDIC<br>SURGEON &amp; PODIATRIST</div>
      <div class="approval__label">APPROVED BY</div>
      <span class="approval__seal"></span>
    </div>
  </section>
</main>
</body>
</html>
```